Need UI design for an iOS app game with most of the layout planned

The name of the game is "QUADRIX".

The goal of the game is to find a way to manipulate four numbers so that the end result is 24. Addition, subtraction, multiplication and division may be used and each number can only be used once.

The list of items we need is:

1. launch image, app icon, UI design of all scenes (10-12 scenes) of the app.
2. App background image should support screen size of both 640x1136.
3. Files are preferred to be in (.eps) format so that resolution can be adjusted later. But other file formats are welcome as long as resolution is high enough.
4. Icons, buttons, background image etc. should have their own file so that later they can be moved around in case design is changed.

The detailed requirement is in the attached file. The actual layout can vary if it can help achieve better result. We also attached several screenshots from iOS game "Glimbo". You can use that as your reference.

```html
<!DOCTYPE html>
<html lang="en">
<head>
<meta charset="utf-8">
<title>QUADRIX – Main Menu</title>
<link rel="stylesheet" href="https://fonts.googleapis.com/css2?family=Nunito:wght@900&family=Roboto:wght@500&display=swap">
<style>
  :root {
    --stage-bg: #8fdcf2;
    --screen-blue-top: #2a86d6;
    --screen-blue-bottom: #1565c0;
    --status-bg: rgba(5, 30, 70, 0.55);
    --status-text: #e8f1fb;
    --round-button: #1e7fd0;
    --round-button-ring: #66b6f0;
    --icon-white: #ffffff;
    --orange-light-top: #ffb320;
    --orange-light-bottom: #ff8c00;
    --orange-deep-top: #ff8a10;
    --orange-deep-bottom: #f25a05;
    --logo-tile: #ff7a10;
    --label-white: #ffffff;
  }
  * { box-sizing: border-box; margin: 0; padding: 0; }
  html, body {
    width: 1200px; height: 1200px; overflow: hidden;
    background: var(--stage-bg);
  }
  .stage {
    position: relative; width: 1200px; height: 1200px;
    background: var(--stage-bg);
  }
  .app-screen {
    position: absolute; left: 307px; top: 80px;
    width: 586px; height: 1040px; overflow: hidden;
  }
  .screen-background {
    position: absolute; inset: 0;
    background: radial-gradient(ellipse at 50% 30%, var(--screen-blue-top), var(--screen-blue-bottom) 80%);
  }
  .status-bar {
    position: absolute; left: 0; top: 0; width: 100%; height: 37px;
    background: var(--status-bg);
    color: var(--status-text);
    font: 500 20px "Roboto", sans-serif;
    display: flex; align-items: center; justify-content: space-between;
    padding: 0 14px;
  }
  .carrier { display: flex; align-items: center; gap: 8px; letter-spacing: 0.5px; }
  .signal { display: flex; align-items: flex-end; gap: 2px; height: 14px; }
  .signal span { width: 3px; background: var(--status-text); }
  .battery {
    width: 40px; height: 18px; border: 2px solid var(--status-text); border-radius: 3px;
    padding: 2px; position: relative;
  }
  .battery::before { content: ""; display: block; width: 100%; height: 100%; background: var(--status-text); }
  .battery::after {
    content: ""; position: absolute; right: -6px; top: 4px; width: 3px; height: 6px;
    background: var(--status-text);
  }
  .round-button {
    position: absolute; top: 62px; width: 80px; height: 80px; border-radius: 50%;
    background: var(--round-button);
    box-shadow: inset 0 0 0 4px var(--round-button-ring), 0 4px 10px rgba(0,0,0,0.25);
    display: flex; align-items: center; justify-content: center;
  }
  .settings-button { left: 28px; }
  .info-button { right: 28px; }
  .game-title {
    position: absolute; left: 0; top: 290px; width: 100%;
    display: flex; align-items: center; justify-content: center; gap: 18px;
  }
  .title-tile {
    width: 56px; height: 56px; border-radius: 10px; background: var(--logo-tile);
  }
  .title-name {
    font: 900 64px "Nunito", sans-serif; color: var(--label-white); letter-spacing: 1px;
  }
  .menu {
    position: absolute; left: 73px; top: 600px; width: 440px;
    display: flex; flex-direction: column; gap: 26px;
  }
  .menu-button {
    height: 86px; border-radius: 14px;
    display: flex; align-items: center; justify-content: center;
    font: 900 38px "Nunito", sans-serif; color: var(--label-white);
    text-shadow: 0 2px 2px rgba(120, 40, 0, 0.45);
    box-shadow: 0 6px 14px rgba(0, 0, 0, 0.3);
  }
  .menu-button.single { background: linear-gradient(var(--orange-light-top), var(--orange-light-bottom)); }
  .menu-button.multi { background: linear-gradient(var(--orange-deep-top), var(--orange-deep-bottom)); }
</style>
</head>
<body>
<main class="stage">
  <section class="app-screen">
    <div class="screen-background" role="img" aria-label="Blue blueprint grid background with light rays from the centre"></div>

    <header class="status-bar">
      <div class="carrier">
        <div class="signal"><span style="height:4px"></span><span style="height:7px"></span><span style="height:10px"></span><span style="height:14px"></span></div>
        CARRIER
      </div>
      <div class="battery"></div>
    </header>

    <div class="round-button settings-button" aria-label="Settings">
      <svg width="44" height="44" viewBox="0 0 44 44">
        <g fill="var(--icon-white)" transform="translate(22 22)">
          <rect x="-4" y="-20" width="8" height="10" rx="1"/>
          <rect x="-4" y="-20" width="8" height="10" rx="1" transform="rotate(45)"/>
          <rect x="-4" y="-20" width="8" height="10" rx="1" transform="rotate(90)"/>
          <rect x="-4" y="-20" width="8" height="10" rx="1" transform="rotate(135)"/>
          <rect x="-4" y="-20" width="8" height="10" rx="1" transform="rotate(180)"/>
          <rect x="-4" y="-20" width="8" height="10" rx="1" transform="rotate(225)"/>
          <rect x="-4" y="-20" width="8" height="10" rx="1" transform="rotate(270)"/>
          <rect x="-4" y="-20" width="8" height="10" rx="1" transform="rotate(315)"/>
          <circle r="14"/>
        </g>
        <circle cx="22" cy="22" r="6" fill="var(--round-button)"/>
      </svg>
    </div>

    <div class="round-button info-button" aria-label="Information">
      <svg width="50" height="50" viewBox="0 0 50 50">
        <circle cx="25" cy="25" r="21" fill="none" stroke="var(--icon-white)" stroke-width="4"/>
        <circle cx="25" cy="14" r="3.5" fill="var(--icon-white)"/>
        <rect x="21.5" y="20" width="7" height="18" rx="2" fill="var(--icon-white)"/>
      </svg>
    </div>

    <div class="game-title">
      <div class="title-tile"></div>
      <h1 class="title-name">QUADRIX</h1>
    </div>

    <nav class="menu">
      <div class="menu-button single">Single Player</div>
      <div class="menu-button multi">Multiplayer</div>
    </nav>
  </section>
</main>
</body>
</html>
```